KLT, Inc. business card desing

Design a business card for an contemporary e commerce company that sells fragrances and cosmetics. State of the art , high tech and super very fast delivery

Target Market(s)

e commerce customers like Bramble, Tolvex , and retailers wesites

Industry/Entity Type

Business

Contact Information for Business Card

On the Front :

scentharborline.example with some design element

On the back :
Dr. Marek Thornby
President

Phone ( icom) 555.207.6431
Cell (icon) 555.284.9062
Fax(icon) 555.613.4870
email (icon) marek@scentharborline.example

4815 Cedar Lane
Ronkonkoma, NY 11990

Colors
b768aa
e667a6
abd036

Requirements
Must have
• all the above content info
Nice to have
• Could have and abstract perfume bottle
Should not have
• no faces, facial features,

```html
<!DOCTYPE html>
<html lang="en">
<head>
<meta charset="utf-8">
<title>Business Card</title>
<link rel="stylesheet" href="https://fonts.googleapis.com/css2?family=Figtree:wght@500;600&display=swap">
<style>
  :root {
    --page-bg: #f4f4f4;
    --card-bg: #231f20;
    --card-edge: #8c8a8a;
    --accent-pink: #e0409b;
    --bottle-tone: #34272b;
  }
  * { margin: 0; padding: 0; box-sizing: border-box; }
  html, body {
    width: 1200px;
    height: 403px;
    overflow: hidden;
    background: var(--page-bg);
  }
  .canvas {
    position: relative;
    width: 1200px;
    height: 403px;
    font-family: "Figtree", "Helvetica Neue", Arial, sans-serif;
    font-weight: 500;
    color: var(--accent-pink);
    letter-spacing: 1.5px;
  }
  .card {
    position: absolute;
    width: 505px;
    height: 290px;
    background: var(--card-bg);
    box-shadow: 0 1px 1px rgba(0,0,0,0.35);
    overflow: hidden;
  }
  .card--front { left: 39px; top: 54px; }
  .card--back  { left: 628px; top: 53px; border: 1px solid var(--card-edge); }

  .bottle-art {
    position: absolute;
    left: 128px;
    top: 18px;
    width: 250px;
    height: 258px;
    border-radius: 45% 45% 40% 40%;
    background: radial-gradient(ellipse at 45% 50%, var(--bottle-tone) 0%, rgba(52,39,43,0.6) 45%, rgba(35,31,32,0) 72%);
  }
  .front-domain {
    position: absolute;
    left: 0;
    width: 100%;
    top: 131px;
    text-align: center;
    font-size: 21px;
    font-weight: 600;
    letter-spacing: 2.1px;
  }

  .identity {
    position: absolute;
    left: 58px;
    top: 22px;
    font-size: 16px;
    line-height: 24px;
    font-weight: 600;
  }
  .contact-list {
    position: absolute;
    left: 24px;
    top: 93px;
    list-style: none;
    font-size: 16px;
    line-height: 24px;
  }
  .contact-item {
    display: flex;
    align-items: center;
    height: 24px;
  }
  .contact-icon {
    width: 18px;
    height: 16px;
    margin-right: 16px;
    fill: var(--accent-pink);
    flex: none;
  }
  .address {
    position: absolute;
    right: 18px;
    top: 226px;
    text-align: right;
    font-size: 16px;
    line-height: 24px;
    font-style: normal;
  }
</style>
</head>
<body>
<main class="canvas">

  <section class="card card--front" aria-label="Card front">
    <div class="bottle-art" role="img" aria-label="Faint abstract perfume bottle with drifting scent swirls"></div>
    <p class="front-domain">ScentHarborLine.example</p>
  </section>

  <section class="card card--back" aria-label="Card back">
    <div class="identity">
      <p class="identity-name">Dr. Marek Thornby</p>
      <p class="identity-title">President</p>
    </div>

    <ul class="contact-list">
      <li class="contact-item">
        <svg class="contact-icon" viewBox="0 0 18 16" aria-label="Phone" role="img">
          <path d="M4.2 1.5c.5-.3 1.1-.2 1.4.3l1.4 2.3c.3.5.2 1.1-.2 1.4l-1 .8c.7 1.6 2 2.9 3.6 3.7l.8-1c.4-.4 1-.5 1.4-.2l2.3 1.4c.5.3.6.9.3 1.4l-.8 1.3c-.4.6-1.1.9-1.8.7C7.6 12.6 4.4 9.4 3.4 5.4c-.2-.7.1-1.4.7-1.8z"/>
        </svg>
        <span>555.207.6431</span>
      </li>
      <li class="contact-item">
        <svg class="contact-icon" viewBox="0 0 18 16" aria-label="Mobile" role="img">
          <path d="M6.5 2h5a1 1 0 0 1 1 1v10a1 1 0 0 1-1 1h-5a1 1 0 0 1-1-1V3a1 1 0 0 1 1-1zm.5 1.4v8.2h4V3.4zM9 12.2a.6.6 0 1 0 0 1.2.6.6 0 0 0 0-1.2z"/>
        </svg>
        <span>555.284.9062</span>
      </li>
      <li class="contact-item">
        <svg class="contact-icon" viewBox="0 0 18 16" aria-label="Fax" role="img">
          <path d="M5 1.5h7v3.5H5z M2 6h14a1 1 0 0 1 1 1v6.5a1 1 0 0 1-1 1H2a1 1 0 0 1-1-1V7a1 1 0 0 1 1-1zm2 2v1.3h4V8zm0 2.4v1.3h4v-1.3z"/>
        </svg>
        <span>555.613.4870</span>
      </li>
      <li class="contact-item">
        <svg class="contact-icon" viewBox="0 0 18 16" aria-label="Email" role="img">
          <path d="M1 3h16v1.2L9 9 1 4.2z M1 5.8l8 4.8 8-4.8V13H1z"/>
        </svg>
        <span>marek@scentharborline.example</span>
      </li>
    </ul>

    <address class="address">
      <p>4815 Cedar Lane</p>
      <p>Fernhollow, NY 11990</p>
    </address>
  </section>

</main>
</body>
</html>
```